Business card Zottelgarten

Business card is for a self-employed dog trainer with own dog school. Name and logo of the dog school are available. Color specifications as well. The design should be classy and minimalist, but also modern. An already existing idea would be: Front: Only the logo Back: Contact data

Font styles to use
Serif
Sans Serif
Other font styles liked:
• Trajan Pro

Colors
f78f20

Requirements
Must have
• Name: Margit Wendler-Rasch Title: Dipl. Dog Trainer Contain my logo Follow my font and color preferences (see files)

```html
<!DOCTYPE html>
<html lang="de">
<head>
<meta charset="utf-8">
<title>Zottelgarten – Visitenkarte</title>
<link rel="stylesheet" href="https://fonts.googleapis.com/css2?family=Cinzel:wght@400;500&display=swap">
<style>
  :root {
    --brand-orange: #f78f20;
    --paper: #ffffff;
    --ink: #1c1c1c;
    --backdrop: #eceded;
    --card-shadow: rgba(0, 0, 0, 0.18);
  }
  * { margin: 0; padding: 0; box-sizing: border-box; }
  html, body {
    width: 1200px;
    height: 1200px;
    overflow: hidden;
    background: var(--backdrop);
    font-family: "Cinzel", "Times New Roman", serif;
  }
  .canvas {
    position: relative;
    width: 1200px;
    height: 1200px;
  }
  .card {
    position: absolute;
    width: 720px;
    height: 440px;
    box-shadow: 0 6px 18px var(--card-shadow);
  }

  /* Front */
  .card-front {
    left: 70px;
    top: 80px;
    background: var(--brand-orange);
    color: var(--paper);
    display: flex;
    flex-direction: column;
    align-items: center;
  }
  .brand-circle {
    margin-top: 40px;
    width: 250px;
    height: 250px;
  }
  .brand-name {
    margin-top: 18px;
    font-size: 62px;
    font-weight: 400;
    letter-spacing: 2px;
    line-height: 1;
    text-transform: uppercase;
  }
  .brand-web {
    margin-top: 10px;
    font-size: 17px;
    letter-spacing: 9px;
    text-transform: uppercase;
  }

  /* Back */
  .card-back {
    left: 410px;
    top: 640px;
    background: var(--paper);
    text-align: center;
    padding-top: 44px;
  }
  .person-name {
    color: var(--brand-orange);
    font-size: 40px;
    font-weight: 400;
    line-height: 1.1;
  }
  .person-title {
    color: var(--brand-orange);
    font-size: 28px;
    font-weight: 400;
    margin-top: 6px;
  }
  .contact-list {
    list-style: none;
    margin-top: 34px;
    color: var(--ink);
    font-size: 27px;
    line-height: 48px;
  }
</style>
</head>
<body>
<main class="canvas">
  <section class="card card-front" aria-label="Vorderseite">
    <svg class="brand-circle" viewBox="0 0 250 250" aria-hidden="true">
      <circle cx="125" cy="125" r="125" fill="#ffffff"/>
    </svg>
    <h1 class="brand-name">Zottelgarten</h1>
    <p class="brand-web">www.zottelgarten.ch</p>
  </section>

  <section class="card card-back" aria-label="Rückseite">
    <h2 class="person-name">Margit Wendler-Rasch</h2>
    <p class="person-title">Dipl. Hundetrainerin</p>
    <ul class="contact-list">
      <li>Adresse</li>
      <li>Stadt</li>
      <li>Telefonnummer</li>
      <li>Email</li>
      <li>Webseite</li>
    </ul>
  </section>
</main>
</body>
</html>
```